Podcast Cover Art for Alliance Growth Circle

We need a podcast cover design for a podcast called "Alliance Growth Circle". The podcast is about partnerships in the enterprise software business. The "cover design" is kind of like an album cover and there's a great article here about how to create a stunning Podcast cover art:

https://www.wavelumen.com/blog/10-tips-create-awesome-podcast-artwork

There are also examples in that post linked above.

The Alliance Growth Circle already has some design themes/elements that I'll attach a background image for reference so you can see the typical colors, fonts, etc.

The cover art should include the words "Alliance Growth Circle" and include the names of the two artists:

Derek Halvor
Trevor Lindqvist

It should also include the Alliance Growth Circle logo somewhere. I'll attach that.

I've attached the fonts used for the logo text.

I'll also attach photos of the two artists (2 options to choose from for each). We need your guidance on whether we should include those in some stylized way, or leave them out.

Thanks for the help!

Technical Specifications:

Square Image
3000 x 3000 pixels
Resolution of 72 dpi
PNG or JPEG file types
Colorspace RGB

Colors
0054AA
0677BA
7BADD7
CADEEF
E8F1F8

Requirements
Should not have
• Avoid overused images like microphones and headsets

```html
<!DOCTYPE html>
<html lang="en">
<head>
<meta charset="utf-8">
<title>Alliance Growth Circle – Podcast Cover</title>
<link rel="stylesheet" href="https://fonts.googleapis.com/css2?family=Montserrat:wght@600;700;800&family=Great+Vibes&display=swap">
<style>
  :root {
    --navy-deep: #061a5c;
    --navy: #0a2a8c;
    --royal: #0054aa;
    --ocean: #0677ba;
    --sky: #7badd7;
    --mist: #cadeef;
    --frost: #e8f1f8;
    --signal: #e4ff0a;
    --band: #0b3fb0;
    --stroke: #0b5cc4;
  }
  html, body {
    margin: 0;
    width: 1200px;
    height: 1200px;
    overflow: hidden;
    background: #ffffff;
  }
  .cover {
    position: relative;
    width: 1200px;
    height: 1200px;
    overflow: hidden;
    background:
      radial-gradient(ellipse 420px 380px at 600px 220px, rgba(123,173,215,0.55), transparent 70%),
      radial-gradient(ellipse 700px 600px at 600px 400px, rgba(6,119,186,0.55), transparent 75%),
      linear-gradient(160deg, var(--navy) 0%, var(--royal) 45%, var(--navy-deep) 75%, #1a1a8a 100%);
  }
  .cover__backdrop {
    position: absolute;
    inset: 0;
  }
  .host-photo {
    position: absolute;
  }
  .host-photo--left {
    left: 85px; top: 68px; width: 545px; height: 562px;
    background: linear-gradient(180deg, #5a6c8a 0%, #8a99ae 55%, #b9c6d6 100%);
    clip-path: polygon(32% 0, 68% 0, 74% 60%, 100% 72%, 100% 100%, 0 100%, 0 72%, 26% 60%);
  }
  .host-photo--right {
    left: 621px; top: 50px; width: 501px; height: 545px;
    background: linear-gradient(180deg, #9a8a7c 0%, #caa48e 40%, #1c2236 72%, #11162a 100%);
    clip-path: polygon(22% 0, 68% 0, 74% 58%, 100% 70%, 100% 100%, 0 100%, 0 70%, 20% 58%);
  }
  .brand-mark {
    position: absolute;
    left: 1006px; top: 76px;
    width: 160px;
    display: flex;
    flex-direction: column;
    align-items: center;
    gap: 8px;
  }
  .brand-mark__dot {
    width: 58px; height: 58px;
    border-radius: 50%;
    background: var(--mist);
  }
  .brand-mark__name {
    font-family: "Montserrat", sans-serif;
    font-weight: 700;
    font-size: 13px;
    line-height: 1.2;
    color: var(--mist);
    text-align: center;
    text-transform: uppercase;
    letter-spacing: 0.04em;
  }
  .title-stroke {
    position: absolute;
    left: 41px; top: 650px;
    width: 1117px; height: 230px;
    background: var(--stroke);
    border-radius: 6px;
  }
  .title {
    position: absolute;
    left: 0; width: 1200px;
    margin: 0;
    text-align: center;
    font-family: "Montserrat", sans-serif;
    font-weight: 800;
    line-height: 1;
    text-shadow: 4px 5px 8px rgba(0, 10, 50, 0.55);
  }
  .title__line {
    position: absolute;
    left: 0; width: 1200px;
    display: block;
  }
  .title__line--top {
    top: 545px;
    font-size: 176px;
    letter-spacing: -0.01em;
    color: var(--mist);
  }
  .title__line--middle {
    top: 718px;
    font-size: 146px;
    letter-spacing: 0.02em;
    color: var(--mist);
  }
  .title__line--bottom {
    top: 840px;
    font-size: 124px;
    letter-spacing: 0.02em;
    color: var(--signal);
  }
  .hosts-label {
    position: absolute;
    left: 0; width: 1200px;
    top: 999px;
    margin: 0;
    text-align: center;
    font-family: "Montserrat", sans-serif;
    font-weight: 600;
    font-size: 46px;
    color: var(--frost);
    line-height: 1;
  }
  .hosts-band {
    position: absolute;
    left: 0; top: 1070px;
    width: 1200px; height: 101px;
    background: linear-gradient(90deg, rgba(10,40,140,0.65) 0%, var(--band) 50%, var(--band) 100%);
  }
  .hosts-names {
    position: absolute;
    left: 0; width: 1200px;
    top: 1078px;
    margin: 0;
    text-align: center;
    font-family: "Great Vibes", cursive;
    font-size: 70px;
    line-height: 1.2;
    color: var(--frost);
    text-shadow: 2px 3px 4px rgba(0, 10, 50, 0.6);
  }
</style>
</head>
<body>
  <main class="cover">
    <div class="cover__backdrop" role="img" aria-label="Abstract glowing blue light-streak background"></div>

    <div class="host-photo host-photo--left" role="img" aria-label="Portrait photo of host Trevor Lindqvist in a light grey shirt"></div>
    <div class="host-photo host-photo--right" role="img" aria-label="Portrait photo of host Derek Halvor in a dark blazer and light shirt"></div>

    <div class="brand-mark">
      <span class="brand-mark__dot"></span>
      <span class="brand-mark__name">Alliance Growth Circle</span>
    </div>

    <div class="title-stroke" role="img" aria-label="Blue paint-brush stroke behind the title"></div>

    <h1 class="title">
      <span class="title__line title__line--top">ALLIANCE</span>
      <span class="title__line title__line--middle">GROWTH</span>
      <span class="title__line title__line--bottom">CIRCLE</span>
    </h1>

    <p class="hosts-label">Hosted By:</p>
    <div class="hosts-band"></div>
    <p class="hosts-names">Trevor Lindqvist &amp; Derek Halvor</p>
  </main>
</body>
</html>
```